Letterhead Design Project

Looking for letterhead designs for Dravesco Mining.

I am looking for a letterhead design in conjunction with a business card design. I have opened contests for both but ask that if you submit a letterhead design you also submit a business card design with a corresponding look/feel.

Dravesco Mining is a B2B company that buys and sells large machinery tires within the coal mining industry. The design should the strong, crisp and masculine. I have uploaded the company logo and mock-up of the back of the company's business card.

Color scheme should be grey/green/black

Contact information to include:
Name: Tom Sealbrook
Title: Managing Director
Phone: 555-314-2097
Address: 1186 Pelham #3 Dallas, TX 75209
Email: Tom@Dravesco.example

Project Deadline Extended
Reason: Looking for a more refined, elegant letterhead than what's been submitted as of yet. Here is a sample of what we're looking for: http://www.plumbridgestudio.example/letterhead-designs/ We will also be increasing the payment.

```html
<!DOCTYPE html>
<html lang="en">
<head>
<meta charset="utf-8">
<title>Dravesco Mining – Stationery</title>
<link rel="stylesheet" href="https://fonts.googleapis.com/css2?family=Open+Sans:wght@400;600;700&family=Dancing+Script:wght@500&display=swap">
<style>
  :root{
    --bg:#eeeeee;
    --paper:#ffffff;
    --ink:#3a3a3a;
    --ink-soft:#555555;
    --brand-grey:#4a4a4a;
    --brand-green:#5fa132;
    --card-dark:#2e2e2e;
    --signature:#2d3a78;
  }
  *{box-sizing:border-box;margin:0;padding:0}
  html,body{width:1200px;height:800px;overflow:hidden;background:var(--bg)}
  body{position:relative;font-family:"Open Sans",Arial,sans-serif;color:var(--ink)}

  .brand{display:flex;align-items:center;gap:8px}
  .brand-square{width:22px;height:22px;background:var(--brand-green);flex:none}
  .brand-name{font-weight:700;color:var(--brand-grey);letter-spacing:.5px;white-space:nowrap}

  /* Letterhead */
  .letterhead{position:absolute;left:235px;top:82px;width:460px;height:647px;background:var(--paper);
    box-shadow:0 2px 6px rgba(0,0,0,.08)}
  .letterhead .brand{position:absolute;left:33px;top:38px}
  .letterhead .brand-name{font-size:22px}
  .letterhead .brand-square{width:26px;height:26px}
  .lh-contact{position:absolute;left:328px;top:33px;font-size:6.6px;line-height:9.6px;color:var(--ink);font-style:normal}
  .lh-contact .company{font-weight:700}
  .contact-line{display:flex;align-items:center;gap:6px;white-space:nowrap}
  .contact-line svg{width:6px;height:6px;fill:var(--brand-green);flex:none}
  .lh-body{position:absolute;left:40px;top:146px;width:385px;font-size:9.1px;line-height:13px;color:var(--ink)}
  .lh-body .salutation{font-weight:600;margin-bottom:17px}
  .lh-body p{text-align:justify;margin-bottom:13px}
  .lh-sign{position:absolute;left:40px;top:500px}
  .lh-sign .signature{font-family:"Dancing Script",cursive;font-size:28px;color:var(--signature);line-height:30px}
  .lh-sign .title{font-size:9.5px;color:var(--ink);margin-top:2px}
  .lh-web{position:absolute;left:0;right:0;bottom:17px;text-align:center;font-size:7px;letter-spacing:.6px;color:var(--ink)}
  .lh-tab{position:absolute;left:128px;bottom:0;width:238px;height:12px;background:var(--brand-green);border-radius:5px 5px 0 0}

  /* Cards */
  .card{position:absolute;width:198px;height:112px;box-shadow:0 2px 5px rgba(0,0,0,.12);overflow:hidden}

  /* Card front */
  .card-front{left:768px;top:443px;background:var(--card-dark)}
  .card-front .brand{position:absolute;left:0;right:0;top:44px;justify-content:center;gap:7px}
  .card-front .brand-name{color:#f2f2f2;font-size:12px;letter-spacing:.4px}
  .card-front .brand-square{width:15px;height:15px}
  .card-front .web{position:absolute;left:0;right:0;top:84px;text-align:center;font-size:5.6px;color:#e0e0e0;letter-spacing:.4px}
  .card-front .tab{position:absolute;left:43px;bottom:0;width:112px;height:7px;background:var(--brand-green);border-radius:3px 3px 0 0}

  /* Card back */
  .card-back{left:764px;top:612px;width:200px;height:114px;background:var(--paper)}
  .card-back .brand{position:absolute;left:18px;top:22px;gap:6px}
  .card-back .brand-name{font-size:11px}
  .card-back .brand-square{width:13px;height:13px}
  .card-back .marker{position:absolute;left:0;top:56px;width:5px;height:14px;background:var(--brand-green)}
  .card-back .person{position:absolute;left:18px;top:57px;font-size:6.6px;line-height:7.5px}
  .card-back .person .role{font-size:4.4px;letter-spacing:.2px;color:var(--ink-soft)}
  .card-back .details{position:absolute;left:18px;top:80px;font-size:5.6px;line-height:8.6px}
  .card-back .contact-line{gap:5px}
  .card-back .contact-line svg{width:5px;height:5px}
</style>
</head>
<body>

<section class="letterhead" aria-label="Letterhead">
  <div class="brand">
    <span class="brand-square"></span>
    <span class="brand-name">DRAVESCO MINING</span>
  </div>

  <address class="lh-contact">
    <div class="company">Dravesco Mining</div>
    <div>1186 Pelham #3 Dallas, TX 75209</div>
    <div class="contact-line"><svg viewBox="0 0 10 10"><path d="M2 0h2l1 3-1.5 1a6 6 0 0 0 2.5 2.5L7 5l3 1v2a2 2 0 0 1-2 2A8 8 0 0 1 0 2a2 2 0 0 1 2-2z"/></svg>555-314-2097</div>
    <div class="contact-line"><svg viewBox="0 0 10 10"><path d="M0 2h10v7H0zM1 3l4 3 4-3z"/></svg>Tom@Dravesco.example</div>
  </address>

  <div class="lh-body">
    <div class="salutation">Lorem Ipsum,</div>
    <p>Lorem ipsum dolor sit amet, consectetur adipisicing elit, sed do eiusmod tempor incididunt ut labore et dolore magna aliqua. Ut enim ad minim veniam, quis nostrud exercitation ullamco laboris nisi ut aliquip ex ea commodo consequat.</p>
    <p>Duis aute irure dolor in reprehenderit in voluptate velit esse cillum dolore eu fugiat nulla pariatur. Excepteur sint occaecat cupidatat non proident, sunt in culpa qui officia deserunt mollit anim id est laborum.</p>
    <p>Sed ut perspiciatis unde omnis iste natus error sit voluptatem accusantium doloremque laudantium, totam rem aperiam, eaque ipsa quae ab illo inventore veritatis et quasi architecto beatae vitae dicta sunt explicabo.</p>
    <p>Nemo enim ipsam voluptatem quia voluptas sit aspernatur aut odit aut fugit, sed quia consequuntur magni dolores eos qui ratione voluptatem sequi nesciunt. Neque porro quisquam est, qui dolorem ipsum quia dolor sit amet, consectetur, adipisci velit, sed quia non numquam eius modi tempora incidunt ut labore et dolore magnam aliquam quaerat voluptatem.</p>
    <p>Ut enim ad minima veniam, quis nostrum exercitationem ullam corporis suscipit laboriosam, nisi ut aliquid ex ea commodi consequatur?</p>
    <p>Quis autem vel eum iure reprehenderit qui in ea voluptate velit esse quam nihil molestiae consequatur, vel illum qui dolorem eum fugiat quo voluptas nulla pariatur?</p>
  </div>

  <div class="lh-sign">
    <div class="signature">Tom Sealbrook</div>
    <div class="title">MANAGING DIRECTOR</div>
  </div>

  <div class="lh-web">www.Dravesco.example</div>
  <div class="lh-tab"></div>
</section>

<section class="card card-front" aria-label="Business card front">
  <div class="brand">
    <span class="brand-square"></span>
    <span class="brand-name">DRAVESCO MINING</span>
  </div>
  <div class="web">www.Dravesco.example</div>
  <div class="tab"></div>
</section>

<section class="card card-back" aria-label="Business card back">
  <div class="brand">
    <span class="brand-square"></span>
    <span class="brand-name">DRAVESCO MINING</span>
  </div>
  <div class="marker"></div>
  <div class="person">
    <div>Tom Sealbrook</div>
    <div class="role">MANAGING DIRECTOR</div>
  </div>
  <div class="details">
    <div class="contact-line"><svg viewBox="0 0 10 10"><path d="M2 0h2l1 3-1.5 1a6 6 0 0 0 2.5 2.5L7 5l3 1v2a2 2 0 0 1-2 2A8 8 0 0 1 0 2a2 2 0 0 1 2-2z"/></svg>555-314-2097</div>
    <div class="contact-line"><svg viewBox="0 0 10 10"><path d="M0 2h10v7H0zM1 3l4 3 4-3z"/></svg>Tom@Dravesco.example</div>
    <div class="contact-line"><svg viewBox="0 0 10 10"><path d="M5 0a3.5 3.5 0 0 1 3.5 3.5C8.5 6 5 10 5 10S1.5 6 1.5 3.5A3.5 3.5 0 0 1 5 0zm0 2a1.5 1.5 0 1 0 0 3 1.5 1.5 0 0 0 0-3z"/></svg>1186 Pelham #3 Dallas, TX 75209</div>
  </div>
</section>

</body>
</html>
```